Retail Info Signage

I would need a redesign of a current retail sign for the store, same colors if possible, the fonts and the border just need a full rework and has to be a HIGH DPI over 1000 in order for me to manipulate the size of the banner. One is a 24×72 landscape design the other is a portrait information design. 24x 30.

Target Market(s)

Shipping, Packing, Retail Customers

Industry/Entity Type

Shipping/Packing/Retail

Font styles to use
Sans Serif
Decorative

Colors
0054AA
0677BA
7BADD7
CADEEF
E8F1F8
EB3D1F
EC4F4E
F09395
F8D3D4
FCEDEE

Requirements
Must have
• The colors associated with the initial design that needs rework
Nice to have
• Elegant, consistent, not too formal but informative
Should not have
• No clip art will provide logo for design if needed

```html
<!DOCTYPE html>
<html lang="en">
<head>
<meta charset="utf-8">
<title>Brisk Pack &amp; Ship Durham – Services</title>
<link rel="stylesheet" href="https://fonts.googleapis.com/css2?family=Kanit:ital,wght@1,900&family=Lobster&family=Nunito:wght@800;900&family=Montserrat:wght@300;400;700;800&display=swap">
<style>
  :root{
    --blue:#0054AA;
    --blue-mid:#0677BA;
    --blue-light:#7BADD7;
    --blue-pale:#E8F1F8;
    --red:#EB3D1F;
    --red-bright:#F0151B;
    --white:#FFFFFF;
  }
  *{margin:0;padding:0;box-sizing:border-box}
  html,body{width:1200px;height:400px;overflow:hidden;background:var(--white)}
  .sign{position:relative;width:1200px;height:400px;overflow:hidden;background:var(--white);font-family:"Nunito",sans-serif}
  .backdrop{position:absolute;inset:0}
  .brand-mark{position:absolute;left:30px;top:14px;width:80px;height:68px;display:flex;flex-direction:column;align-items:center;justify-content:center;gap:6px}
  .brand-mark .mark-square{width:26px;height:26px;border:3px solid var(--white)}
  .brand-mark .mark-name{font-family:"Montserrat",sans-serif;font-weight:800;font-size:18px;color:var(--white);letter-spacing:2px}
  .store-title{position:absolute;left:150px;top:20px;width:690px;font-family:"Kanit",sans-serif;font-style:italic;font-weight:900;font-size:47px;line-height:1;color:var(--white);letter-spacing:0;white-space:nowrap}
  .tagline{position:absolute;right:22px;top:24px;font-family:"Lobster",cursive;font-size:24px;line-height:31px;color:var(--white);text-align:right;white-space:nowrap}
  .services-heading{position:absolute;left:27px;top:108px;width:373px;height:37px;border:3px solid var(--red-bright);display:flex;align-items:center;padding-left:12px;font-family:"Montserrat",sans-serif;font-size:24px;color:var(--red-bright);letter-spacing:4px;white-space:nowrap;overflow:hidden}
  .services-heading b{font-weight:800;margin-right:14px}
  .services-heading span{font-weight:300}
  .heading-rule{position:absolute;left:400px;top:125px;width:448px;height:1.5px;background:var(--red-bright)}
  .section-tag{position:absolute;height:21px;background:var(--red-bright);color:var(--white);font-family:"Montserrat",sans-serif;font-weight:400;font-size:14px;line-height:21px;padding-left:10px;clip-path:polygon(0 0,100% 0,calc(100% - 8px) 100%,0 100%);white-space:nowrap}
  .service-list{position:absolute;list-style:none}
  .service-list li{position:relative;padding-left:23px;font-weight:900;font-size:15.5px;line-height:20px;color:var(--blue);white-space:nowrap}
  .service-list li svg{position:absolute;left:0;top:3px;width:15px;height:15px}
  .service-list .highlight{color:var(--red-bright)}
  .flag-block{display:inline-block;width:24px;height:12px;vertical-align:-1px;background:linear-gradient(180deg,#1A3D9C 50%,#D21F2A 50%)}
  .carriers-tag{position:absolute;left:912px;top:163px;width:244px;height:27px;background:var(--red-bright);color:var(--white);font-family:"Montserrat",sans-serif;font-weight:800;font-size:17px;line-height:27px;text-align:center;clip-path:polygon(10px 0,100% 0,calc(100% - 10px) 100%,0 100%)}
  .carrier{position:absolute;display:flex;align-items:center;gap:6px;width:145px;font-family:"Montserrat",sans-serif;font-weight:800;color:var(--blue);font-size:14px;line-height:15px}
  .carrier i{display:block;flex:none;width:13px;height:13px;background:var(--blue)}
  .carrier.small{font-size:12px}
  .contact-row{position:absolute;right:22px;top:357px;display:flex;gap:14px;align-items:center;font-family:"Montserrat",sans-serif;font-weight:400;font-size:11px;color:var(--white);white-space:nowrap}
  .contact-row span{display:flex;align-items:center;gap:5px}
  .contact-row .dot{width:13px;height:13px;border-radius:50%;background:var(--white)}
</style>
</head>
<body>
<main class="sign">
  <svg class="backdrop" width="1200" height="400" viewBox="0 0 1200 400" aria-hidden="true">
    <polygon points="0,0 960,0 955,10 0,10" fill="var(--blue)"/>
    <polygon points="0,0 145,0 145,15 895,15 858,90 145,90 110,97 0,97" fill="var(--blue)"/>
    <polygon points="130,80 866,80 858,90 115,90" fill="var(--blue-light)"/>
    <polygon points="858,24 898,24 868,90 858,90" fill="var(--blue-light)"/>
    <polygon points="960,0 1200,0 1200,135 900,135" fill="var(--red-bright)"/>
    <polygon points="945,0 953,0 893,135 885,135" fill="var(--red-bright)"/>
    <polygon points="895,138 1200,138 1200,345 805,345" fill="var(--blue-pale)"/>
    <line x1="900" y1="125" x2="820" y2="260" stroke="var(--red-bright)" stroke-width="3"/>
    <line x1="878" y1="150" x2="778" y2="360" stroke="var(--red-bright)" stroke-width="1.5"/>
    <polygon points="800,345 1200,345 1200,400 770,400" fill="var(--red-bright)"/>
    <polygon points="355,388 790,388 785,400 350,400" fill="var(--blue)"/>
    <rect x="0" y="396" width="355" height="4" fill="var(--red-bright)"/>
    <polygon points="768,400 800,330 803,330 772,400" fill="var(--blue)"/>
  </svg>

  <div class="brand-mark" aria-label="BPS">
    <i class="mark-square"></i><span class="mark-name">BPS</span>
  </div>
  <h1 class="store-title">BRISK PACK &amp; SHIP DURHAM</h1>
  <p class="tagline">“Your Mailing &amp;<br>Business Service Center<br>for over 20 Years”</p>

  <h2 class="services-heading"><b>SERVICES</b><span>OFFERED:</span></h2>
  <div class="heading-rule"></div>

  <svg width="0" height="0" style="position:absolute" aria-hidden="true">
    <symbol id="tick" viewBox="0 0 16 16">
      <circle cx="8" cy="8" r="6.5" fill="none" stroke="#F0151B" stroke-width="1.8"/>
      <path d="M4.5 8.2 L7.3 11 L15 3" fill="none" stroke="#F0151B" stroke-width="2.2" stroke-linecap="round" stroke-linejoin="round"/>
    </symbol>
  </svg>

  <div class="section-tag" style="left:28px;top:161px;width:257px">PACKING &amp; SHIPPING SERVICES</div>
  <ul class="service-list" style="left:28px;top:189px">
    <li><svg><use href="#tick"/></svg>SPECIALIZED CUSTOM<br>BOX/<span class="highlight">BALIKBAYAN BOXES</span> <span class="flag-block" role="img" aria-label="Philippine flag"></span></li>
    <li><svg><use href="#tick"/></svg>PROFESSIONAL PACKING</li>
    <li><svg><use href="#tick"/></svg>PACKAGING SUPPLIES</li>
    <li><svg><use href="#tick"/></svg>DOMESTIC SHIPPING</li>
    <li><svg><use href="#tick"/></svg>INTERNATIONAL SHIPPING</li>
  </ul>

  <div class="section-tag" style="left:25px;top:319px;width:181px">PRINTING SERVICES</div>
  <ul class="service-list" style="left:28px;top:345px">
    <li><svg><use href="#tick"/></svg>FLYERS &amp; BROCHURES</li>
    <li><svg><use href="#tick"/></svg>BUSINESS CARDS</li>
  </ul>

  <ul class="service-list" style="left:312px;top:185px">
    <li><svg><use href="#tick"/></svg>LARGE FORMAT PRINTING</li>
    <li><svg><use href="#tick"/></svg>NEWSLETTER PRINTING</li>
    <li><svg><use href="#tick"/></svg>INKPRINT (FINGERPRINTING)</li>
    <li><svg><use href="#tick"/></svg>DIRECT MAILERS PRINTING</li>
    <li><svg><use href="#tick"/></svg>PHOTOGRAPHY</li>
    <li><svg><use href="#tick"/></svg>ARCHITECTURAL</li>
    <li><svg><use href="#tick"/></svg>BLUEPRINT BANNERS</li>
    <li><svg><use href="#tick"/></svg>ARTWORK</li>
    <li><svg><use href="#tick"/></svg>COPYING &amp; FAXING</li>
  </ul>

  <div class="section-tag" style="left:589px;top:160px;width:248px">HOME &amp; BUSINESS SERVICES</div>
  <ul class="service-list" style="left:589px;top:187px">
    <li><svg><use href="#tick"/></svg>NOTARY SERVICES</li>
    <li><svg><use href="#tick"/></svg>PASSPORT SERVICES</li>
    <li><svg><use href="#tick"/></svg>OFFICE SUPPLIES</li>
    <li><svg><use href="#tick"/></svg>EVERGREEN STAMPS</li>
    <li><svg><use href="#tick"/></svg>CUSTOM STAMP MAKERS</li>
    <li><svg><use href="#tick"/></svg>KEY MAKING SERVICES</li>
    <li><svg><use href="#tick"/></svg>VIRTUAL MAILBOXES</li>
    <li><svg><use href="#tick"/></svg>MAILBOX RENTAL</li>
    <li><svg><use href="#tick"/></svg>GIFT SHOP RETAIL</li>
  </ul>

  <div class="carriers-tag">DELIVERY CARRIERS</div>
  <div class="carrier" style="left:895px;top:226px;width:125px"><i></i>PARCELWAY</div>
  <div class="carrier small" style="left:1035px;top:219px"><i></i>NATIONAL MAIL<br>SERVICE</div>
  <div class="carrier" style="left:895px;top:286px;width:125px"><i></i>SWIFTLINE</div>
  <div class="carrier" style="left:1035px;top:286px"><i></i>GLOBEX</div>

  <div class="contact-row">
    <span><i class="dot"></i>@bpsdurham</span>
    <span><i class="dot"></i>bpsdurham.com</span>
    <span><svg width="17" height="12" viewBox="0 0 17 12" aria-hidden="true"><rect x="0.75" y="0.75" width="15.5" height="10.5" fill="none" stroke="#fff" stroke-width="1.5"/><path d="M1 1 L8.5 7 L16 1" fill="none" stroke="#fff" stroke-width="1.5"/></svg>hello@bpsdurham.com</span>
  </div>
</main>
</body>
</html>
```